Silver Ridge Business Card Design

I have an existing corporate logo. I'd like to clean it up bit (sharpen it up) and make it look better (without major redesign). I'd like to get the logo itself in all major file formats for print, web, etc.
Then I'd like a business card design that reflects a strategy consulting firm. It should be clean - logo and text without major graphics, and perhaps some small color treatments that match the logo color. The card should suggest high quality in terms of the company.
I'd like the files for card in all major print formats.
Target Market(s)
Silver Ridge Partners is a strategy development and business consulting firm focused on small to mid-sized companies. We specialize in business strategy, comprehensive business plan development, market segmentation and positioning, financial models, marketing and sales strategy, product strategy and the effective use of social media in business growth. We operate as consultants, advisers, retained members of management teams, and Board members. We often serve in the role of Chief Strategy Officer, supporting CEO's and other senior executives to enhance top and bottom line growth.
Our overall approach with clients is to deliver actual results, and we often take an active team role with business founders and management teams to drive business growth and affect real changes in performance. As a result, we approach each situation uniquely and partner with clients in a manner that will have the biggest impact on enterprise value.
Business
Look and feel

```html
<!DOCTYPE html>
<html lang="en">
<head>
<meta charset="utf-8">
<title>Silver Ridge Partners – Business Cards</title>
<link href="https://fonts.googleapis.com/css2?family=Libre+Franklin:wght@400;600;700;800&display=swap" rel="stylesheet">
<style>
  :root {
    --bg: #2a2a2a;
    --bg-edge: #141414;
    --brand-blue: #1d8fd0;
    --band-light: #3aa6e0;
    --band-dark: #0f6fb0;
    --swoosh-gray: #6e6e6e;
    --card-white: #ffffff;
    --card-black: #050505;
    --name-gray: #7a7a7a;
    --name-black: #111111;
    --text-white: #ffffff;
    --icon-gray: #8a8a8a;
    --icon-dark: #1a1a1a;
  }
  * { box-sizing: border-box; margin: 0; padding: 0; }
  html, body { width: 1200px; height: 800px; overflow: hidden; }
  body {
    background: radial-gradient(ellipse at 50% 40%, var(--bg) 0%, var(--bg-edge) 100%);
    font-family: "Libre Franklin", Arial, sans-serif;
    position: relative;
  }
  .card {
    position: absolute;
    top: 263px;
    width: 480px;
    height: 274px;
    border-radius: 22px;
    overflow: hidden;
    box-shadow: 0 6px 14px rgba(0,0,0,0.55);
  }
  .card--light { left: 100px; background: var(--card-white); }
  .card--dark { left: 623px; background: var(--card-black); }
  .card__art { position: absolute; inset: 0; }
  .wordmark {
    position: absolute;
    left: 34px;
    top: 54px;
    display: flex;
    align-items: center;
    gap: 12px;
  }
  .wordmark__dot {
    width: 30px;
    height: 30px;
    border-radius: 50%;
    background: var(--brand-blue);
    flex: none;
  }
  .wordmark__name {
    font-size: 22px;
    font-weight: 600;
    line-height: 1;
    color: var(--brand-blue);
  }
  .person { position: absolute; left: 38px; top: 175px; color: var(--text-white); }
  .person__name { font-size: 20px; font-weight: 800; line-height: 1; }
  .card--light .person__name { color: var(--name-gray); }
  .card--dark .person__name { color: var(--name-black); }
  .person__title { font-size: 12px; margin-top: 5px; }
  .person__address { font-size: 12px; margin-top: 14px; line-height: 16px; }
  .contacts { position: absolute; left: 280px; top: 174px; list-style: none; color: var(--text-white); font-size: 12.5px; }
  .contacts li { display: flex; align-items: center; height: 17px; }
  .contacts svg { width: 10px; height: 10px; margin-right: 6px; flex: none; }
  .contacts .contacts__web { font-weight: 700; }
  .card--light .contacts svg { color: var(--icon-gray); }
  .card--dark .contacts svg { color: var(--icon-dark); }
</style>
</head>
<body>

<div class="card card--light">
  <svg class="card__art" viewBox="0 0 480 274" aria-hidden="true">
    <defs>
      <linearGradient id="bandLight" x1="0" y1="0" x2="0" y2="1">
        <stop offset="0" stop-color="#3aa6e0"/>
        <stop offset="1" stop-color="#0f6fb0"/>
      </linearGradient>
    </defs>
    <path d="M0 137 Q230 168 480 142 L480 274 L0 274 Z" fill="url(#bandLight)"/>
    <path d="M150 152 Q330 150 480 128 L480 138 Q330 158 150 152 Z" fill="#6e6e6e"/>
  </svg>
  <div class="wordmark"><span class="wordmark__dot"></span><span class="wordmark__name">Silver Ridge Partners</span></div>
  <div class="person">
    <p class="person__name">Mark D. Hallen</p>
    <p class="person__title">Partner and Founder</p>
    <p class="person__address">412 Birchwood Lane<br>Lakemont, Illinois 60491</p>
  </div>
  <ul class="contacts">
    <li><svg viewBox="0 0 10 10"><path fill="currentColor" d="M2 0h3l1 2-1.5 1.5a6 6 0 0 0 2 2L8 4l2 1v3c0 1-1 2-2 2C4 10 0 6 0 2 0 1 1 0 2 0z"/></svg>312.555.0148</li>
    <li><svg viewBox="0 0 10 10"><rect fill="currentColor" x="0" y="2" width="10" height="6.5"/><path d="M0 2l5 3.5L10 2" stroke="#fff" stroke-width="0.8" fill="none"/></svg>mark@srpartners.com</li>
    <li class="contacts__web"><svg viewBox="0 0 10 10"><circle fill="currentColor" cx="5" cy="5" r="5"/><path d="M0 5h10M5 0c-2.5 3-2.5 7 0 10M5 0c2.5 3 2.5 7 0 10" stroke="#fff" stroke-width="0.6" fill="none"/></svg>www.srpartners.com</li>
    <li><svg viewBox="0 0 10 10"><rect fill="currentColor" width="10" height="10" rx="1.5"/></svg>network.com/in/mhallen</li>
    <li><svg viewBox="0 0 10 10"><rect fill="currentColor" width="10" height="10" rx="1.5"/></svg>@MarkHallen</li>
  </ul>
</div>

<div class="card card--dark">
  <svg class="card__art" viewBox="0 0 480 274" aria-hidden="true">
    <defs>
      <linearGradient id="bandDark" x1="0" y1="0" x2="0" y2="1">
        <stop offset="0" stop-color="#3aa6e0"/>
        <stop offset="1" stop-color="#0f6fb0"/>
      </linearGradient>
    </defs>
    <path d="M0 137 Q230 168 480 142 L480 274 L0 274 Z" fill="url(#bandDark)"/>
    <path d="M150 152 Q330 150 480 128 L480 138 Q330 158 150 152 Z" fill="#6e6e6e"/>
  </svg>
  <div class="wordmark"><span class="wordmark__dot"></span><span class="wordmark__name">Silver Ridge Partners</span></div>
  <div class="person">
    <p class="person__name">Mark D. Hallen</p>
    <p class="person__title">Partner and Founder</p>
    <p class="person__address">412 Birchwood Lane<br>Lakemont, Illinois 60491</p>
  </div>
  <ul class="contacts">
    <li><svg viewBox="0 0 10 10"><path fill="currentColor" d="M2 0h3l1 2-1.5 1.5a6 6 0 0 0 2 2L8 4l2 1v3c0 1-1 2-2 2C4 10 0 6 0 2 0 1 1 0 2 0z"/></svg>312.555.0148</li>
    <li><svg viewBox="0 0 10 10"><rect fill="currentColor" x="0" y="2" width="10" height="6.5"/><path d="M0 2l5 3.5L10 2" stroke="#3aa6e0" stroke-width="0.8" fill="none"/></svg>mark@srpartners.com</li>
    <li class="contacts__web"><svg viewBox="0 0 10 10"><circle fill="currentColor" cx="5" cy="5" r="5"/><path d="M0 5h10M5 0c-2.5 3-2.5 7 0 10M5 0c2.5 3 2.5 7 0 10" stroke="#3aa6e0" stroke-width="0.6" fill="none"/></svg>www.srpartners.com</li>
    <li><svg viewBox="0 0 10 10"><rect fill="currentColor" width="10" height="10" rx="1.5"/></svg>network.com/in/mhallen</li>
    <li><svg viewBox="0 0 10 10"><rect fill="currentColor" width="10" height="10" rx="1.5"/></svg>@MarkHallen</li>
  </ul>
</div>

</body>
</html>
```